Brochure Design Project

I need a presentation folder with two inside pages and a pocket on back cover, use use my logo ,
make the cover just using the logo (put it big and centered, then use the logo in the background to fill, read the brief and make it modern, stop trying to make it exactly like the picture I gave as sample please use your talent trust your self
I just uploaded text for presentation folder
Dr's offices and patients

```html
<!DOCTYPE html>
<html lang="en">
<head>
<meta charset="utf-8">
<title>Steadfast Recovery Counseling Agency – Folder Cover</title>
<link href="https://fonts.googleapis.com/css2?family=Lato:wght@300&display=swap" rel="stylesheet">
<style>
  :root {
    --paper: #ffffff;
    --ink: #1f1f1f;
    --accent: #9a5a30;
    --brown-deep: #8a5532;
    --brown-mid: #b8977f;
    --brown-soft: #e9dfd7;
    --grey-mid: #bdbdbd;
    --grey-soft: #eeeeee;
    --mark: #9c6440;
  }
  html, body {
    margin: 0;
    padding: 0;
    width: 848px;
    height: 1200px;
    overflow: hidden;
    background: var(--paper);
  }
  .cover {
    position: relative;
    width: 848px;
    height: 1200px;
    overflow: hidden;
    background: var(--paper);
    font-family: "Lato", "Helvetica Neue", Arial, sans-serif;
  }
  .decoration {
    position: absolute;
    left: 0;
    top: 0;
    width: 848px;
    height: 1200px;
  }
  .brand-dot {
    position: absolute;
    left: 50px;
    top: 40px;
    width: 130px;
    height: 130px;
    border-radius: 50%;
    background: var(--mark);
  }
  .brand-name {
    position: absolute;
    left: 342px;
    top: 58px;
    margin: 0;
    font-weight: 300;
    font-size: 38px;
    line-height: 46px;
    letter-spacing: 0.1px;
    color: var(--ink);
    white-space: nowrap;
  }
  .brand-name span { display: block; }
  .brand-name .brand-lead { color: var(--accent); }
</style>
</head>
<body>
  <main class="cover">
    <svg class="decoration" viewBox="0 0 848 1200" role="img" aria-label="Large radial arrangement of the agency symbol in warm brown and soft grey tones filling the lower cover">
      <defs>
        <radialGradient id="warm-bloom" cx="0" cy="700" r="480" gradientUnits="userSpaceOnUse">
          <stop offset="0" stop-color="var(--brown-deep)" stop-opacity="0.92"/>
          <stop offset="0.55" stop-color="var(--brown-mid)" stop-opacity="0.75"/>
          <stop offset="1" stop-color="var(--brown-soft)" stop-opacity="0.55"/>
        </radialGradient>
        <radialGradient id="cool-bloom" cx="848" cy="700" r="450" gradientUnits="userSpaceOnUse">
          <stop offset="0" stop-color="var(--grey-mid)" stop-opacity="0.75"/>
          <stop offset="1" stop-color="var(--grey-soft)" stop-opacity="0.45"/>
        </radialGradient>
      </defs>
      <circle class="bloom bloom-cool" cx="848" cy="700" r="450" fill="url(#cool-bloom)"/>
      <circle class="bloom bloom-warm" cx="0" cy="700" r="480" fill="url(#warm-bloom)"/>
    </svg>

    <header class="brand">
      <div class="brand-dot" aria-hidden="true"></div>
      <h1 class="brand-name"><span class="brand-lead">steadfast</span><span>recovery counseling agency</span></h1>
    </header>
  </main>
</body>
</html>
```